SaaS Pricing Model / Product Features Infographic

Background: We are Brightwave, a communications platform designed for large groups, leadership, and democracy. Our customers may be non-profits, schools, student groups, unions, businesses, and other types of communities, along with elected leaders.

We need a pricing model infographic that we can give to our web developer for implementation on our website. It should outline the different features we have for each of our packages and provide the user with a simple way of comparing our service offerings side-by-side. The primary use of this infographic will be on the website. We have two components of the infographic - the group tier (free/silver/gold/platinum) and the Professional packages (Agency and Enterprise). We need to organize and display the features in an easy-to-read and easy-to-understand way. I would be open to 'collapsed' views *if* recommended/needed, but would prefer not if possible. User will be able to tap on some features to get a pop-up explanation / visualization. An example for inspiration has been attached. The graphic should include our "Brightwave" brand and color scheme along with use of the Roboto font. This will replace the Pricing section of our current (draft) website: https://teklora.example/brightwave/

The secondary use of this infographic will be for print. The primary implementation is a website.

Industry/Entity Type

Leadership

Colors

Designer to choose colors to be used in the design.

Requirements
Must have
• Please see inspiration graphic for general concept. Design and format are completely up to you. Please be sure to include icons next to each item as shown in the inspiration graphic. Should be modern and pop.
Nice to have
• Would be good to align with our color scheme or a complementary color scheme.
Should not have
• Should not feel old, dated, or stale.

```html
<!DOCTYPE html>
<html lang="en">
<head>
<meta charset="utf-8">
<title>Brightwave Pricing Tiers</title>
<link href="https://fonts.googleapis.com/css2?family=Roboto:wght@400;500;700;900&display=swap" rel="stylesheet">
<style>
:root{
  --navy:#05055c;
  --ink:#0b1160;
  --sky:#52c4f5;
  --pale:#bce7fb;
  --shade:#80d1f8;
  --line:#3c4d9a;
  --white:#ffffff;
}
*{box-sizing:border-box;margin:0;padding:0}
html,body{width:1200px;height:997px;overflow:hidden}
body{background:var(--navy);font-family:"Roboto",sans-serif;color:var(--ink);position:relative}

.brand{position:absolute;left:30px;top:98px;display:flex;align-items:center;gap:14px}
.brand-dot{width:30px;height:30px;border-radius:50%;background:var(--sky)}
.brand-name{font-weight:900;font-size:62px;color:var(--white);letter-spacing:-1px}

.tier-badge{position:absolute;width:112px;height:112px;border-radius:50%;border:12px solid var(--sky);background:var(--navy);
  display:flex;align-items:center;justify-content:center;text-align:center;color:var(--sky);font-weight:700;font-size:18px;line-height:1.15;top:28px}
.price-row{position:absolute;left:566px;top:127px;width:600px;height:75px;display:flex;gap:3px}
.price{flex:1;background:var(--sky);display:flex;align-items:center;justify-content:center;text-align:center;
  font-size:14px;font-weight:500;color:var(--ink);position:relative;line-height:1.15}
.price::before{content:"";position:absolute;top:16px;left:50%;margin-left:-6px;border:6px solid transparent;border-top:7px solid var(--navy)}
.price span{padding-top:10px}

.features{position:absolute;left:27px;top:209px;width:1146px;height:754px;background:var(--pale);border-radius:12px;overflow:hidden;padding-top:4px}
.col-shade{position:absolute;top:0;bottom:0;background:var(--shade)}
.col-shade.mission{left:539px;width:149px}
.col-shade.gold{left:839px;width:150px}
.row{position:relative;display:grid;grid-template-columns:539px 149px 151px 150px 157px;height:28.6px;align-items:center;font-size:12.5px;border-bottom:1px solid var(--line)}
.row:last-child{border-bottom:none}
.label{display:flex;align-items:center;gap:0}
.label svg{width:22px;height:22px;margin-left:20px;margin-right:12px;flex:none}
.row.sub .label svg{margin-left:56px;margin-right:31px}
.val{text-align:center}
</style>
</head>
<body>
<svg width="0" height="0" style="position:absolute" aria-hidden="true">
  <defs>
    <symbol id="i-box" viewBox="0 0 24 24"><rect x="3" y="3" width="18" height="18" rx="2" fill="none" stroke="#0b1160" stroke-width="1.6"/><path d="M7 17L17 7M12 7h5v5" fill="none" stroke="#0b1160" stroke-width="1.6"/></symbol>
    <symbol id="i-phone" viewBox="0 0 24 24"><rect x="7" y="2" width="10" height="20" rx="2" fill="none" stroke="#0b1160" stroke-width="1.6"/><circle cx="12" cy="18" r="1" fill="#0b1160"/></symbol>
    <symbol id="i-web" viewBox="0 0 24 24"><rect x="2" y="5" width="20" height="14" rx="1" fill="none" stroke="#0b1160" stroke-width="1.6"/><path d="M2 9h20" stroke="#0b1160" stroke-width="1.6"/></symbol>
    <symbol id="i-bell" viewBox="0 0 24 24"><path d="M6 17V11a6 6 0 0 1 12 0v6l2 2H4z M10 21h4" fill="none" stroke="#0b1160" stroke-width="1.6"/></symbol>
    <symbol id="i-list" viewBox="0 0 24 24"><rect x="4" y="3" width="16" height="18" rx="1" fill="none" stroke="#0b1160" stroke-width="1.6"/><path d="M8 8h8M8 12h8M8 16h8" stroke="#0b1160" stroke-width="1.6"/></symbol>
    <symbol id="i-chat" viewBox="0 0 24 24"><path d="M3 4h15v11H9l-4 4v-4H3z" fill="none" stroke="#0b1160" stroke-width="1.6"/><path d="M7 8h8M7 11h6" stroke="#0b1160" stroke-width="1.6"/></symbol>
    <symbol id="i-cal" viewBox="0 0 24 24"><rect x="3" y="5" width="18" height="16" rx="2" fill="none" stroke="#0b1160" stroke-width="1.6"/><path d="M3 10h18M8 3v4M16 3v4M8 15l3 3 5-5" fill="none" stroke="#0b1160" stroke-width="1.6"/></symbol>
    <symbol id="i-people" viewBox="0 0 24 24"><circle cx="7" cy="7" r="3" fill="none" stroke="#0b1160" stroke-width="1.6"/><circle cx="17" cy="7" r="3" fill="none" stroke="#0b1160" stroke-width="1.6"/><path d="M2 20v-5a5 5 0 0 1 10 0v5M12 20v-5a5 5 0 0 1 10 0v5" fill="none" stroke="#0b1160" stroke-width="1.6"/></symbol>
    <symbol id="i-chart" viewBox="0 0 24 24"><path d="M3 19l6-7 4 4 8-10" fill="none" stroke="#0b1160" stroke-width="1.6"/><circle cx="3" cy="19" r="1.5" fill="#0b1160"/><circle cx="21" cy="6" r="1.5" fill="#0b1160"/></symbol>
    <symbol id="i-mail" viewBox="0 0 24 24"><rect x="4" y="5" width="16" height="11" fill="none" stroke="#0b1160" stroke-width="1.6"/><path d="M2 19h20M4 5l8 6 8-6" fill="none" stroke="#0b1160" stroke-width="1.6"/></symbol>
    <symbol id="i-sliders" viewBox="0 0 24 24"><path d="M6 3v18M12 3v18M18 3v18" stroke="#0b1160" stroke-width="1.6"/><circle cx="6" cy="8" r="2" fill="#bce7fb" stroke="#0b1160" stroke-width="1.6"/><circle cx="12" cy="15" r="2" fill="#bce7fb" stroke="#0b1160" stroke-width="1.6"/><circle cx="18" cy="10" r="2" fill="#bce7fb" stroke="#0b1160" stroke-width="1.6"/></symbol>
    <symbol id="i-gear" viewBox="0 0 24 24"><circle cx="12" cy="12" r="6" fill="none" stroke="#0b1160" stroke-width="1.6" stroke-dasharray="3 2"/><circle cx="12" cy="12" r="2.5" fill="none" stroke="#0b1160" stroke-width="1.6"/></symbol>
    <symbol id="i-star" viewBox="0 0 24 24"><path d="M12 2l2 4 4 .5-3 3 .8 4-3.8-2-3.8 2 .8-4-3-3 4-.5z" fill="#0b1160"/><rect x="3" y="15" width="18" height="7" fill="none" stroke="#0b1160" stroke-width="1.6"/></symbol>
    <symbol id="i-card" viewBox="0 0 24 24"><rect x="2" y="5" width="20" height="15" rx="1" fill="none" stroke="#0b1160" stroke-width="1.6"/><circle cx="8" cy="11" r="2" fill="none" stroke="#0b1160" stroke-width="1.6"/><path d="M5 17a3 3 0 0 1 6 0M14 10h5M14 14h5" fill="none" stroke="#0b1160" stroke-width="1.6"/></symbol>
    <symbol id="i-shield" viewBox="0 0 24 24"><rect x="2" y="3" width="20" height="18" fill="none" stroke="#0b1160" stroke-width="1.6"/><path d="M12 7l5 2v3c0 3-2 5-5 6-3-1-5-3-5-6V9z" fill="none" stroke="#0b1160" stroke-width="1.6"/></symbol>
    <symbol id="i-roster" viewBox="0 0 24 24"><rect x="2" y="2" width="20" height="20" rx="2" fill="none" stroke="#0b1160" stroke-width="1.8"/><path d="M6 7h2M6 12h2M6 17h2M11 7h7M11 12h7M11 17h7" stroke="#0b1160" stroke-width="2"/></symbol>
    <symbol id="i-sync" viewBox="0 0 24 24"><circle cx="12" cy="12" r="9" fill="none" stroke="#0b1160" stroke-width="1.6"/><path d="M8 12l3 3 5-6" fill="none" stroke="#0b1160" stroke-width="1.6"/></symbol>
    <symbol id="i-bars" viewBox="0 0 24 24"><path d="M4 21V12M9 21V6M14 21V10M19 21V4M2 21h20" stroke="#0b1160" stroke-width="2.2"/></symbol>
  </defs>
</svg>

<header class="brand">
  <span class="brand-dot"></span>
  <span class="brand-name">Brightwave</span>
</header>

<div class="tier-badge" style="left:585px">Mission<br>Tier</div>
<div class="tier-badge" style="left:736px">Silver<br>Tier</div>
<div class="tier-badge" style="left:886px">Gold<br>Tier</div>
<div class="tier-badge" style="left:1035px">Platinum<br>Tier</div>

<div class="price-row">
  <div class="price"><span>FREE for any groups<br>and elected officials</span></div>
  <div class="price"><span>$19/month</span></div>
  <div class="price"><span>$39/month</span></div>
  <div class="price"><span>$149/month</span></div>
</div>

<section class="features">
  <div class="col-shade mission"></div>
  <div class="col-shade gold"></div>

  <div class="row"><div class="label"><svg><use href="#i-box"/></svg>Size Limit</div><div class="val">Unlimited</div><div class="val">1000 group members</div><div class="val">5000 group members</div><div class="val">Unlimited</div></div>
  <div class="row"><div class="label"><svg><use href="#i-phone"/></svg>Mobile App</div><div class="val">Free</div><div class="val">Free</div><div class="val">Free</div><div class="val">Free</div></div>
  <div class="row"><div class="label"><svg><use href="#i-web"/></svg>Web App</div><div class="val">Free</div><div class="val">Free</div><div class="val">Free</div><div class="val">Free</div></div>
  <div class="row"><div class="label"><svg><use href="#i-bell"/></svg>Push Notification Alerts for all Group Leader created content including:</div><div class="val">Y</div><div class="val">Y</div><div class="val">Y</div><div class="val">Y</div></div>
  <div class="row sub"><div class="label"><svg><use href="#i-list"/></svg>Unlimited Group Polls</div><div class="val">Y</div><div class="val">Y</div><div class="val">Y</div><div class="val">Y</div></div>
  <div class="row sub"><div class="label"><svg><use href="#i-web"/></svg>Unlimited Group Petitions</div><div class="val">Y</div><div class="val">Y</div><div class="val">Y</div><div class="val">Y</div></div>
  <div class="row sub"><div class="label"><svg><use href="#i-chat"/></svg>Unlimited Group Discussions</div><div class="val">Y</div><div class="val">Y</div><div class="val">Y</div><div class="val">Y</div></div>
  <div class="row sub"><div class="label"><svg><use href="#i-list"/></svg>Unlimited Group Fundraisers</div><div class="val">Y</div><div class="val">Y</div><div class="val">Y</div><div class="val">Y</div></div>
  <div class="row sub"><div class="label"><svg><use href="#i-gear"/></svg>Unlimited Group Crowdfunders</div><div class="val">Y</div><div class="val">Y</div><div class="val">Y</div><div class="val">Y</div></div>
  <div class="row sub"><div class="label"><svg><use href="#i-cal"/></svg>Unlimited Group Events</div><div class="val">Y</div><div class="val">Y</div><div class="val">Y</div><div class="val">Y</div></div>
  <div class="row sub"><div class="label"><svg><use href="#i-bell"/></svg>Unlimited Group Announcements</div><div class="val">N</div><div class="val">N</div><div class="val">N</div><div class="val">Y</div></div>
  <div class="row"><div class="label"><svg><use href="#i-people"/></svg>All Group Members Linked to Elected Leaders</div><div class="val">Y</div><div class="val">Y</div><div class="val">Y</div><div class="val">Y</div></div>
  <div class="row"><div class="label"><svg><use href="#i-card"/></svg>Customizable Group Profile</div><div class="val">Y</div><div class="val">Y</div><div class="val">Y</div><div class="val">Y</div></div>
  <div class="row"><div class="label"><svg><use href="#i-chart"/></svg>Basic Analytics</div><div class="val">Y</div><div class="val">Y</div><div class="val">Y</div><div class="val">Y</div></div>
  <div class="row"><div class="label"><svg><use href="#i-chart"/></svg>Accountability Metrics</div><div class="val">Y</div><div class="val">Y</div><div class="val">Y</div><div class="val">Y</div></div>
  <div class="row"><div class="label"><svg><use href="#i-mail"/></svg>Group E-mail Listserv</div><div class="val">Y</div><div class="val">Y</div><div class="val">Y</div><div class="val">Y</div></div>
  <div class="row"><div class="label"><svg><use href="#i-sliders"/></svg>Listserv Controls</div><div class="val">N</div><div class="val">Y</div><div class="val">Y</div><div class="val">Y</div></div>
  <div class="row"><div class="label"><svg><use href="#i-gear"/></svg>Assign Group Manager privileges</div><div class="val">Y</div><div class="val">Y</div><div class="val">Y</div><div class="val">Y</div></div>
  <div class="row"><div class="label"><svg><use href="#i-star"/></svg>Manual Post Boosting for Group Managers</div><div class="val">Y</div><div class="val">Y</div><div class="val">Y</div><div class="val">Y</div></div>
  <div class="row"><div class="label"><svg><use href="#i-card"/></svg>Membership Posting Controls</div><div class="val">-</div><div class="val">Y</div><div class="val">Y</div><div class="val">Y</div></div>
  <div class="row"><div class="label"><svg><use href="#i-shield"/></svg>Optional Passcode-protected Group Join</div><div class="val">-</div><div class="val">Y</div><div class="val">Y</div><div class="val">Y</div></div>
  <div class="row"><div class="label"><svg><use href="#i-roster"/></svg>Group Membership Roster</div><div class="val">-</div><div class="val">Y</div><div class="val">Y</div><div class="val">Y</div></div>
  <div class="row"><div class="label"><svg><use href="#i-sliders"/></svg>Advanced Group Controls</div><div class="val">-</div><div class="val">Y</div><div class="val">Y</div><div class="val">Y</div></div>
  <div class="row"><div class="label"><svg><use href="#i-people"/></svg>Subgroups</div><div class="val">-</div><div class="val">Y</div><div class="val">Y</div><div class="val">Y</div></div>
  <div class="row"><div class="label"><svg><use href="#i-sync"/></svg>3rd Party Integrations</div><div class="val">-</div><div class="val">-</div><div class="val">-</div><div class="val">Coming Soon</div></div>
  <div class="row"><div class="label"><svg><use href="#i-bars"/></svg>Advanced Analytics</div><div class="val">-</div><div class="val">-</div><div class="val">-</div><div class="val">Coming Soon</div></div>
</section>
</body>
</html>
```